依頼詳細
病院にて使用する封筒デザインの募集です
記載項目
医療法人 栄樹会 ベルミナ中央病院 BELMINA CENTRAL HOSPITAL
【英語表記は小さめで】

診療科目 内科、呼吸器内科、消化器内科、循環器内科、放射線科、リハビリテーション科、精神科、心療内科

希望イメージ
シンプル 複雑
単色 カラフル
暗い 明るい
日常 高級
遊び心 厳粛
未来的 伝統的
女性的 男性的
希望する色
自由な発想でご提案ください
納品ファイル
• 高解像度JPG (.jpg)
• イラストレーター形式 (.ai)
• フォトショップ形式 (.psd)
補足説明
A4が入る大封筒と
通常サイズの小封筒の2種類をご提案下さい

看板のデザインも募集しておりますので
合わせてご応募頂けると助かります
住所電話番号を追記します

住所 鹿児島県鹿児島市緑葉台2丁目37番8号
TEL 099-555-0142
FAX 099-555-0143
角2(240×332mm)と長3(120×235mm)
でお願い致します

aiファイルも追加致します
吹き抜け壁面と受付カウンター裏の写真を追加します
全体の色使いに関してはロゴの色にこだわらずご提案下さい
建物の色や、吹き抜け壁面の色や形をモチーフにしたものでも構いません
よろしくお願い致します
ご提案ありがとうございます
ロゴカラーに沿ったもの、
吹き抜けカラーに沿ったものをご提案頂いておりますが

合わせて病院の外壁色(赤茶と白)
を基調としたものも募集しております
よろしくお願い致します
■ 選んだ理由

病院のイメージにあっていたので選ばせて頂きました

■ 提案者全員のお礼・コメント

たくさんのご提案を頂きありがとうございました
また利用させて頂きます

```html
<!DOCTYPE html>
<html lang="ja">
<head>
<meta charset="utf-8">
<title>ベルミナ中央病院 角2封筒</title>
<link rel="stylesheet" href="https://fonts.googleapis.com/css2?family=Noto+Sans+JP:wght@400;500&display=swap">
<style>
  :root {
    --paper: #ffffff;
    --backdrop: #e9e9e9;
    --teal: #1f8fa6;
    --text: #555a5e;
    --rule: #d6e6e9;
    --fold: #ececec;
  }
  * { margin: 0; padding: 0; box-sizing: border-box; }
  html, body { width: 874px; height: 1200px; overflow: hidden; background: var(--backdrop); }
  .envelope {
    position: relative;
    width: 874px;
    height: 1200px;
    background: var(--paper);
    font-family: "Noto Sans JP", sans-serif;
    color: var(--text);
  }
  .flap-edge {
    position: absolute; left: 0; top: 0; width: 874px; height: 110px;
    border-bottom: 1px solid var(--fold);
  }
  .flap-mark {
    position: absolute; left: 408px; top: 18px;
    width: 36px; height: 36px; border-radius: 50%;
    background: var(--teal);
  }
  .flap-pattern { position: absolute; left: 470px; top: 20px; }
  .corner-pattern { position: absolute; right: 0; top: 850px; }
  .identity {
    position: absolute; left: 44px; top: 925px;
    display: flex; flex-direction: column; align-items: flex-start;
  }
  .identity__mark {
    width: 62px; height: 62px; border-radius: 50%;
    background: var(--teal); margin-bottom: 12px;
  }
  .identity__en {
    font-size: 13px; line-height: 1.4; letter-spacing: 0.04em; color: var(--teal); font-weight: 500;
  }
  .identity__name {
    font-size: 34px; line-height: 1.2; color: var(--teal); font-weight: 500;
    letter-spacing: 0.02em;
  }
  .identity__corp {
    font-size: 12px; line-height: 1.4; color: var(--teal);
    align-self: flex-end; margin-top: 4px;
  }
  .contact {
    position: absolute; left: 44px; right: 44px; top: 1118px;
    font-size: 10.5px; line-height: 1.9; color: var(--text);
    border-top: 1px solid var(--rule); padding-top: 8px;
  }
</style>
</head>
<body>
<main class="envelope">
  <div class="flap-edge"></div>
  <div class="flap-mark" aria-hidden="true"></div>
  <svg class="flap-pattern" width="260" height="60" viewBox="0 0 260 60" role="img" aria-label="青と緑の三角形モザイク模様">
    <defs>
      <linearGradient id="flapGrad" x1="0" y1="0" x2="1" y2="0">
        <stop offset="0" stop-color="#e4ea8a"/>
        <stop offset="0.45" stop-color="#a6cf4f"/>
        <stop offset="0.75" stop-color="#5fc3c9"/>
        <stop offset="1" stop-color="#2f7fc1"/>
      </linearGradient>
    </defs>
    <polygon points="0,0 260,0 260,30 200,60 120,20 40,20" fill="url(#flapGrad)" opacity="0.7"/>
  </svg>

  <svg class="corner-pattern" width="420" height="250" viewBox="0 0 420 250" role="img" aria-label="青・水色・黄緑の三角形モザイク模様">
    <defs>
      <linearGradient id="cornerGrad" x1="0" y1="1" x2="1" y2="0">
        <stop offset="0" stop-color="#e4ea8a"/>
        <stop offset="0.35" stop-color="#a6cf4f"/>
        <stop offset="0.7" stop-color="#5fc3c9"/>
        <stop offset="1" stop-color="#2f7fc1"/>
      </linearGradient>
    </defs>
    <polygon points="420,0 420,250 60,250 110,180 170,150 210,100 290,80 350,25" fill="url(#cornerGrad)" opacity="0.8"/>
  </svg>

  <section class="identity">
    <div class="identity__mark" aria-hidden="true"></div>
    <p class="identity__en">BELMINA CENTRAL HOSPITAL</p>
    <h1 class="identity__name">ベルミナ中央病院</h1>
    <p class="identity__corp">医療法人 栄樹会</p>
  </section>

  <footer class="contact">
    <p>診療科目／内科、呼吸器内科、消化器内科、循環器内科、放射線科、リハビリテーション科、精神科、心療内科</p>
    <p>医療法人 栄樹会　ベルミナ中央病院　鹿児島県鹿児島市緑葉台2丁目37番8号　TEL 099-555-0142　FAX 099-555-0143</p>
  </footer>
</main>
</body>
</html>
```